Custom Business Card Design

We are looking for a raised spot logo design to use with Tavu.com. We will provide the logo files. Should be a front and back design. We want to implement the house into the back design using the same colors as the logo through out. Something VERY cool!

```html
<!DOCTYPE html>
<html lang="en">
<head>
<meta charset="utf-8">
<title>Tavu Business Card</title>
<link rel="stylesheet" href="https://fonts.googleapis.com/css2?family=Arvo:wght@700&family=Lato:wght@400;700&display=swap">
<style>
  :root {
    --stage: #1d1f22;
    --blue: #2f86c8;
    --blue-light: #3a97d6;
    --blue-deep: #2574b3;
    --red: #e8544a;
    --white: #ffffff;
    --paper: #f2f3f4;
    --ink-blue: #2f7fc1;
  }
  * { box-sizing: border-box; margin: 0; padding: 0; }
  html, body { width: 1200px; height: 1031px; overflow: hidden; }
  body {
    background: var(--stage);
    font-family: "Lato", sans-serif;
    position: relative;
  }
  .card {
    position: absolute;
    width: 560px;
    height: 320px;
    border-radius: 4px;
    overflow: hidden;
    box-shadow: 0 12px 30px rgba(0,0,0,.45);
  }
  /* Front */
  .card--front {
    left: 90px; top: 150px;
    background: linear-gradient(135deg, var(--blue-light) 0%, var(--blue) 55%, var(--blue-deep) 100%);
  }
  .brand {
    position: absolute;
    left: 0; right: 0;
    display: flex; justify-content: center; align-items: center;
  }
  .brand__name {
    font-family: "Arvo", serif;
    font-weight: 700;
    position: relative;
    padding: 6px 24px;
  }
  .brand__name::before, .brand__name::after {
    content: ""; position: absolute; left: 0; right: 0; height: 2px;
    background: currentColor;
  }
  .brand__name::before { top: 0; }
  .brand__name::after { bottom: 0; }
  .card--front .brand { top: 92px; }
  .card--front .brand__name { color: var(--white); font-size: 72px; line-height: 1; padding: 10px 60px; }
  .front__url {
    position: absolute;
    left: 50%; top: 222px;
    transform: translateX(-50%);
    color: var(--white);
    font-size: 16px;
    letter-spacing: .5px;
    border: 2px solid var(--white);
    border-radius: 20px;
    padding: 6px 22px;
  }
  /* Back */
  .card--back {
    left: 550px; top: 560px;
    background: var(--paper);
  }
  .back__shapes { position: absolute; inset: 0; }
  .card--back .brand { left: 30px; right: auto; top: 120px; width: 190px; }
  .card--back .brand__name { color: var(--ink-blue); font-size: 44px; line-height: 1; padding: 8px 22px; }
  .person { position: absolute; left: 350px; top: 30px; color: var(--white); }
  .person__name { font-family: "Arvo", serif; font-weight: 700; font-size: 24px; }
  .person__rule { width: 60px; height: 3px; background: var(--red); margin: 6px 0 5px; }
  .person__title { font-size: 13px; }
  .address {
    position: absolute; left: 350px; top: 120px;
    color: var(--white); font-size: 13px; line-height: 1.5;
    display: flex; gap: 8px;
  }
  .contacts {
    position: absolute; left: 245px; top: 218px;
    list-style: none; color: var(--white); font-size: 13px; line-height: 1.65;
  }
  .contacts li { display: flex; align-items: center; gap: 8px; }
  .icon { width: 12px; height: 12px; flex: none; }
</style>
</head>
<body>

<section class="card card--front" aria-label="Card front">
  <div class="brand"><span class="brand__name">Tavu</span></div>
  <div class="front__url">www.tavu.com</div>
</section>

<section class="card card--back" aria-label="Card back">
  <svg class="back__shapes" viewBox="0 0 560 320" width="560" height="320" aria-hidden="true">
    <defs>
      <linearGradient id="backBlue" x1="0" y1="0" x2="1" y2="1">
        <stop offset="0" stop-color="#3a97d6"/>
        <stop offset="1" stop-color="#2574b3"/>
      </linearGradient>
    </defs>
    <polygon points="305,128 200,190 200,320 222,320 222,178 327,116 327,128" fill="#e8544a"/>
    <polygon points="327,0 560,0 560,320 222,320 222,178 327,116" fill="url(#backBlue)"/>
  </svg>

  <div class="brand"><span class="brand__name">Tavu</span></div>

  <div class="person">
    <div class="person__name">Marcus Ellery</div>
    <div class="person__rule"></div>
    <div class="person__title">CEO/Consultant</div>
  </div>

  <div class="address">
    <svg class="icon" viewBox="0 0 12 12" aria-hidden="true"><path d="M6 0a4 4 0 0 0-4 4c0 3 4 8 4 8s4-5 4-8a4 4 0 0 0-4-4zm0 5.5a1.5 1.5 0 1 1 0-3 1.5 1.5 0 0 1 0 3z" fill="#fff"/></svg>
    <div>4820 Harbor Point Lane<br>Bayside, FL 33199</div>
  </div>

  <ul class="contacts">
    <li><svg class="icon" viewBox="0 0 12 12" aria-hidden="true"><rect x="1" y="1" width="10" height="10" rx="1" fill="none" stroke="#fff" stroke-width="1.2"/></svg>+1-305-555-0148</li>
    <li><svg class="icon" viewBox="0 0 12 12" aria-hidden="true"><path d="M3 1l2 2-1 2c1 1.5 1.5 2 3 3l2-1 2 2-1.5 1.5C5 11 1 7 1.5 2.5z" fill="#fff"/></svg>+1-305-555-0172</li>
    <li><svg class="icon" viewBox="0 0 12 12" aria-hidden="true"><rect x="1" y="2.5" width="10" height="7" fill="none" stroke="#fff" stroke-width="1.2"/><path d="M1 2.5l5 4 5-4" fill="none" stroke="#fff" stroke-width="1.2"/></svg>info@tavu.com</li>
    <li><svg class="icon" viewBox="0 0 12 12" aria-hidden="true"><circle cx="6" cy="6" r="5" fill="none" stroke="#fff" stroke-width="1.2"/><path d="M1 6h10M6 1c-2.5 3-2.5 7 0 10M6 1c2.5 3 2.5 7 0 10" fill="none" stroke="#fff" stroke-width="1"/></svg>www.tavu.com</li>
  </ul>
</section>

</body>
</html>
```